Stationary/business card/envelope design for Larkvale Dentalcare

We are located in the foothills of the sierra nevada mountains. We are looking for a beautiful classy modern stationary. We need evelopes and business card design all to flow seamlessly. Envelope design.

Additional office address 4816 Meridian Wy., Suite B, Auburn, CA 95604 Phone: pending Fax: pending.

3 different Drs on each business card:
Helen R. Marsh, DDS
Orla P. Marsh, DDS
Rebecca S. Halvey, DDS

Target Market(s)

Dental patients

Industry/Entity Type

Dental

Contact Information for Business Card

Two sided. See example.

Font styles to use
Sans Serif

Requirements
Must have
• One sided business cards. Need envelope design.
Colors should match existing logo.

Helen R. Marsh, DDS
Orla P. Marsh, DDS
Rebecca S. Halvey, DDS

```html
<!DOCTYPE html>
<html lang="en">
<head>
<meta charset="utf-8">
<title>Larkvale Dentalcare Stationery</title>
<link href="https://fonts.googleapis.com/css2?family=Questrial&display=swap" rel="stylesheet">
<style>
  :root{
    --green:#1b6e3b;
    --blue:#35a8dc;
    --ink:#555;
    --paper:#ffffff;
    --backdrop:#e8e5e0;
  }
  *{margin:0;padding:0;box-sizing:border-box}
  html,body{width:1200px;height:1200px;overflow:hidden}
  body{background:var(--backdrop);font-family:"Questrial",sans-serif;color:var(--ink);position:relative}
  .sheet{position:absolute;background:var(--paper);box-shadow:0 1px 4px rgba(0,0,0,.15);overflow:hidden}
  .band{position:absolute;left:0;right:0;bottom:0;background:var(--green)}
  .brand{position:absolute;display:flex;align-items:center;gap:4px;color:var(--green);white-space:nowrap}
  .brand .dot{border-radius:50%;background:var(--blue);flex:none}
  .trees{position:absolute;background:linear-gradient(180deg,#2f8a4c,var(--green));border-radius:40% 40% 2px 2px}
  .line{display:flex;align-items:center;gap:4px;white-space:nowrap}
  .line svg{flex:none}

  /* business card */
  .business-card{left:233px;top:121px;width:316px;height:180px}
  .business-card .band{height:9px}
  .business-card .name{position:absolute;left:17px;top:48px;font-size:10.5px;color:var(--blue);font-weight:700}
  .business-card .title{position:absolute;left:17px;top:60px;font-size:7px}
  .business-card .contacts{position:absolute;left:17px;top:82px;font-size:7px;line-height:9.5px}
  .business-card .gap{height:6px}
  .business-card .brand{right:10px;top:24px;font-size:9px;flex-direction:column;gap:3px}
  .business-card .brand .dot{width:42px;height:42px}
  .business-card .trees{right:6px;top:110px;width:55px;height:61px}

  /* appointment card */
  .appointment-card{left:650px;top:121px;width:316px;height:180px}
  .appointment-card .band{height:9px}
  .appointment-card .brand{left:18px;top:24px;font-size:9px;flex-direction:column;gap:3px}
  .appointment-card .brand .dot{width:42px;height:42px}
  .appointment-card .trees{left:6px;top:110px;width:55px;height:61px}
  .appointment-card h2{position:absolute;right:13px;top:21px;font-size:11px;color:var(--green);font-weight:700}
  .appointment-card .days{position:absolute;right:13px;top:49px;font-size:10px;color:var(--blue);line-height:18.7px;text-align:right}
  .appointment-card .days span{display:inline-block;border-bottom:1px solid #555;vertical-align:baseline;height:8px}
  .appointment-card .notice{position:absolute;right:13px;top:146px;font-size:6.5px;color:var(--green);font-weight:700}

  /* envelope front */
  .envelope-front{left:54px;top:493px;width:543px;height:235px}
  .envelope-front .band{height:13px}
  .envelope-front .brand{left:22px;top:134px;font-size:7.5px;flex-direction:column;gap:3px}
  .envelope-front .brand .dot{width:36px;height:36px}
  .envelope-front .address{position:absolute;left:16px;top:197px;font-size:8px}
  .envelope-front .trees{right:8px;top:162px;width:56px;height:59px}

  /* envelope back */
  .envelope-back{left:54px;top:788px;width:543px;height:236px}
  .envelope-back .flap{position:absolute;left:0;top:0}

  /* letterhead */
  .letterhead{left:630px;top:437px;width:510px;height:660px}
  .letterhead .band{height:16px}
  .letterhead .brand{right:24px;top:16px;font-size:10px;flex-direction:column;gap:4px}
  .letterhead .brand .dot{width:66px;height:66px}
  .letterhead .contacts{position:absolute;left:17px;top:538px;font-size:8px;line-height:11px}
  .letterhead .gap{height:12px}
  .letterhead .trees{right:11px;top:576px;width:62px;height:68px}
</style>
</head>
<body>

<section class="sheet business-card">
  <div class="name">Helen R. Marsh, DDS</div>
  <div class="title">Family &amp; Cosmetic Dentistry</div>
  <div class="contacts">
    <div class="line"><svg width="7" height="6" viewBox="0 0 7 6"><rect x="0" y="1" width="7" height="5" rx="1" fill="#35a8dc"/></svg>(530) 555-0142</div>
    <div class="line"><svg width="7" height="6" viewBox="0 0 7 6"><rect x="1" y="0" width="5" height="6" fill="#35a8dc"/></svg>(530) 555-0187</div>
    <div class="gap"></div>
    <div class="line"><svg width="7" height="6" viewBox="0 0 7 6"><rect x="0" y="1" width="7" height="5" fill="#35a8dc"/></svg>larkvaledentalcare@mailbox.com</div>
    <div class="line"><svg width="7" height="7" viewBox="0 0 7 7"><circle cx="3.5" cy="3.5" r="3.5" fill="#35a8dc"/></svg>www.larkvaledentalcare.com</div>
    <div class="gap"></div>
    <div class="line"><svg width="6" height="8" viewBox="0 0 6 8"><path d="M3 8 0.5 4A3 3 0 1 1 5.5 4Z" fill="#35a8dc"/></svg>office 4816 Meridian Wy., Suite B, Auburn, CA 95604</div>
    <div class="line"><svg width="6" height="8" viewBox="0 0 6 8"><path d="M3 8 0.5 4A3 3 0 1 1 5.5 4Z" fill="#35a8dc"/></svg>2270 Cedar Ridge Road, Folsom, California 95631</div>
  </div>
  <div class="brand"><span class="dot"></span>Larkvale Dentalcare</div>
  <div class="trees" role="img" aria-label="Pine tree illustration"></div>
  <div class="band"></div>
</section>

<section class="sheet appointment-card">
  <div class="brand"><span class="dot"></span>Larkvale Dentalcare</div>
  <div class="trees" role="img" aria-label="Pine tree illustration"></div>
  <h2>Your Next Appointment</h2>
  <div class="days">
    <div>Mon <span style="width:78px"></span>at<span style="width:27px"></span></div>
    <div>Tues <span style="width:78px"></span>at<span style="width:27px"></span></div>
    <div>Wed <span style="width:78px"></span>at<span style="width:27px"></span></div>
    <div>Thu <span style="width:84px"></span>at<span style="width:27px"></span></div>
    <div>Fri <span style="width:84px"></span>at<span style="width:27px"></span></div>
  </div>
  <div class="notice">If Unable To Keep Appointment Kindly Give 24 Hour Notice</div>
  <div class="band"></div>
</section>

<section class="sheet envelope-front">
  <div class="brand"><span class="dot"></span>Larkvale Dentalcare</div>
  <div class="address line"><svg width="6" height="8" viewBox="0 0 6 8"><path d="M3 8 0.5 4A3 3 0 1 1 5.5 4Z" fill="#35a8dc"/></svg>2270 Cedar Ridge Road, Folsom, California 95631</div>
  <div class="trees" role="img" aria-label="Pine tree illustration"></div>
  <div class="band"></div>
</section>

<section class="sheet envelope-back">
  <svg class="flap" width="543" height="90" viewBox="0 0 543 90">
    <path d="M0 0H543L528 32Q520 46 500 48L300 84Q272 88 244 84L43 48Q23 46 15 32Z" fill="#1b6e3b" stroke="#111" stroke-width="1"/>
  </svg>
  <div class="trees" role="img" aria-label="White pine tree illustration" style="left:246px;top:22px;width:56px;height:62px;background:#fff"></div>
</section>

<section class="sheet letterhead">
  <div class="brand"><span class="dot"></span>Larkvale Dentalcare</div>
  <div class="contacts">
    <div class="line"><svg width="8" height="7" viewBox="0 0 8 7"><rect x="0" y="1" width="8" height="6" rx="1" fill="#35a8dc"/></svg>(530) 555-0142</div>
    <div class="line"><svg width="8" height="7" viewBox="0 0 8 7"><rect x="1" y="0" width="6" height="7" fill="#35a8dc"/></svg>(530) 555-0187</div>
    <div class="gap"></div>
    <div class="line"><svg width="8" height="7" viewBox="0 0 8 7"><rect x="0" y="1" width="8" height="6" fill="#35a8dc"/></svg>larkvaledentalcare@mailbox.com</div>
    <div class="line"><svg width="8" height="8" viewBox="0 0 8 8"><circle cx="4" cy="4" r="4" fill="#35a8dc"/></svg>www.larkvaledentalcare.com</div>
    <div class="gap"></div>
    <div class="line"><svg width="7" height="9" viewBox="0 0 6 8"><path d="M3 8 0.5 4A3 3 0 1 1 5.5 4Z" fill="#35a8dc"/></svg>office 4816 Meridian Wy., Suite B, Auburn, CA 95604</div>
    <div class="line"><svg width="7" height="9" viewBox="0 0 6 8"><path d="M3 8 0.5 4A3 3 0 1 1 5.5 4Z" fill="#35a8dc"/></svg>2270 Cedar Ridge Road, Folsom, California 95631</div>
  </div>
  <div class="trees" role="img" aria-label="Pine tree illustration"></div>
  <div class="band"></div>
</section>

</body>
</html>
```